Judicial election website to attract voters

I need a simple one-page web design for a judicial election. I'm going to put up one picture, maybe two. The picture I have needs a little touch-up (whiten teeth for example). I have 3 paragraphs of text. I'd like a "Donate" button that can link to a CoinDrift account. I'd also like a little background design, like the Constitution or something like that. There's a couple other little things but that's the bulk of it.

Target Market(s)

Involved voters and some media

Industry/Entity Type

Legal

Number of Pages Required

1 page

Font styles to use
Sans Serif

Requirements
Must have
• My picture, text, donate button
• Phrase "Remember to vote August 30, 2016!"
Nice to have
• Perhaps a second photo, maybe a short 30 second video of me talking directly to the voters, cool background: Constitution, something judgey.
Should not have
• Not sure ... profanity, I guess.

```html
<!DOCTYPE html>
<html lang="en">
<head>
<meta charset="utf-8">
<title>Marianne for Judge</title>
<link href="https://fonts.googleapis.com/css2?family=Alegreya:wght@400;500;700&family=Montserrat:wght@700;800&display=swap" rel="stylesheet">
<style>
  :root{
    --bg-top:#c9c9c9;
    --bg-bottom:#b4b4b4;
    --crimson:#9b1c26;
    --name-red:#c1272d;
    --band:#941b24;
    --ink:#141414;
    --body-ink:#262626;
    --frame:#ffffff;
    --photo-light:#9a9a9a;
    --photo-dark:#5e5e5e;
  }
  *{margin:0;padding:0;box-sizing:border-box}
  html,body{width:961px;height:1200px;overflow:hidden}
  body{background:#fff}
  .page{
    position:relative;width:961px;height:1200px;overflow:hidden;
    background:linear-gradient(180deg,var(--bg-top) 0%,#bebebe 45%,var(--bg-bottom) 100%);
    font-family:"Alegreya",Georgia,serif;
  }
  .backdrop-columns{
    position:absolute;left:0;top:262px;width:490px;height:882px;
    background:linear-gradient(160deg,rgba(255,255,255,.55) 0%,rgba(230,230,230,.35) 35%,rgba(200,200,200,.25) 70%,rgba(180,180,180,.1) 100%);
    clip-path:polygon(0 0,18% 8%,62% 58%,100% 100%,0 100%);
  }
  .headline{position:absolute;color:var(--crimson);font-weight:500;line-height:1;white-space:nowrap}
  .headline--one{left:75px;top:34px;font-size:70px;letter-spacing:-.5px}
  .headline--two{left:245px;top:89px;font-size:119px;letter-spacing:-1.5px}
  .headline--three{left:599px;top:186px;font-size:70px;letter-spacing:-.5px}
  .portrait-frame{
    position:absolute;left:458px;top:284px;width:424px;height:545px;
    background:var(--frame);padding:14px 13px 12px 14px;
    box-shadow:6px 8px 10px rgba(0,0,0,.45);
  }
  .portrait{
    width:100%;height:100%;
    background:radial-gradient(ellipse at 50% 40%,var(--photo-light) 0%,#808080 55%,var(--photo-dark) 100%);
  }
  .name-plate{
    position:absolute;left:119px;top:319px;width:415px;height:90px;
    background:var(--name-red);color:#fff;
    font-family:"Montserrat",Arial,sans-serif;font-weight:800;font-size:72px;
    line-height:90px;padding-left:22px;letter-spacing:.5px;white-space:nowrap;
  }
  .intro{
    position:absolute;right:517px;top:437px;text-align:right;white-space:nowrap;
    font-weight:700;font-size:21px;line-height:26.4px;color:var(--ink);
  }
  .bio{
    position:absolute;text-align:right;white-space:nowrap;
    font-size:16.5px;line-height:20.4px;color:var(--body-ink);
  }
  .bio strong{font-weight:700;color:var(--ink)}
  .bio--service{right:517px;top:720px}
  .bio--courtroom-start{right:517px;top:1068px}
  .bio--courtroom-end{right:79px;top:857px}
  .footer-band{
    position:absolute;left:0;bottom:0;width:961px;height:57px;background:var(--band);
    display:flex;align-items:center;justify-content:space-between;padding:0 60px 0 75px;
  }
  .vote-reminder{color:#fff;font-weight:700;font-size:20px}
  .donate-button{
    display:inline-block;background:#fff;color:var(--band);text-decoration:none;
    font-family:"Montserrat",Arial,sans-serif;font-weight:700;font-size:15px;
    padding:8px 26px;border-radius:4px;letter-spacing:1px;text-transform:uppercase;
  }
</style>
</head>
<body>
<main class="page">
  <div class="backdrop-columns" role="img" aria-label="Faint photograph of a classical courthouse colonnade"></div>

  <h1>
    <span class="headline headline--one">Experienced</span>
    <span class="headline headline--two">Dedicated</span>
    <span class="headline headline--three">Respected</span>
  </h1>

  <figure class="portrait-frame">
    <div class="portrait" role="img" aria-label="Black and white portrait photograph of the candidate smiling"></div>
  </figure>

  <div class="name-plate">Marianne</div>

  <p class="intro">She was born and raised in Tampa<br>Florida, the daughter of an<br>air-conditioning repairman who later<br>opened his own successful business. As<br>the first in her family to go to college, her<br>parents could not have been more proud<br>as she finished her degree at<br>Bayshore University, then continued on<br>to Capital Bay State College of Law<br>where she graduated with honors.</p>

  <p class="bio bio--service">Dedicating her life to public service in central Florida,<br>she has spent the last 18 years as a prosecutor fighting<br>for victims of child abuse and sexual abuse in Orange<br>and Osceola counties. She participates in local<br>charities such as the <strong>Harvest Table Pantry</strong> and<br>the <strong>Open Pages Reading Circle</strong>. Marianne shares her<br>knowledge and experience freely, often mentoring the<br>other young prosecutors and lecturing on jury<br>selection and trial strategies. She is also committed to<br>ensuring ethical behavior in the profession of law. In<br>law school, she won an award for ethics and<br>professionalism but since then she also served as<br><strong>Chair of a Sunshine Bar Grievance Committee</strong>, which<br>handles complaints and ethical violations committed<br>by local attorneys.</p>

  <p class="bio bio--courtroom-start">The cornerstone of Marianne’s candidacy for judge is her<br>experience in the courtroom. Nobody knows how to</p>

  <p class="bio bio--courtroom-end">run an efficient courtroom better than an attorney who has<br>litigated a hundred felony jury trials and argued more<br>pretrial motions than can be counted. But even a judge with<br>all the right knowledge and experience cannot excel without<br>the correct temperament. Ask any attorney or judge who<br>has worked with Marianne and they will tell you that she<br>treats everyone with respect and handles courtroom<br>surprises with a calm head and sense of humor. She would<br>love your support for judge and the opportunity to use her<br>skills and experience to serve <strong>Orange and Osceola County</strong><br>in a new and exciting way.</p>

  <footer class="footer-band">
    <span class="vote-reminder">Remember to vote August 30, 2016!</span>
    <a class="donate-button" href="#donate" aria-label="Donate via CoinDrift">Donate</a>
  </footer>
</main>
</body>
</html>
```